Business Card Design Project

I am looking for a classy business card design for a product design consultancy. We specialize in Product Design, Prototyping, and Manufacturing Consulting. Products that we design range from consumer electronics to household products all the way to sporting goods. We are based in Arizona and called "Heron Design Works." We like to have fun and goof off as much as we like to create new products. We are young and energetic so we would like our business cards to reflect that. We already have a logo that we would like to implement into the card design. A plain rectangular business card is boring so feel free to get creative, but please, no heron shaped cards (it's far too literal). Also feel free to play around with textured card stocks or plastic. The final design that we choose will pay attention to all of the little details. Our cards will need to be 2 sided. We're giving you guys free reign to design as you would like. Please have fun with this, it will reflect in our business card.

Thanks guys,
Heron Design Works Team

Industry/Entity Type

Electronics

Requirements
Must have
• We would like to have a spot UV coating somewhere on the business card design if possible.
Nice to have
• Let's see some designs with custom shapes rather than typical rectangular business cards but please no heron shaped cards, thanks. Also play around with textured card socks.

```html
<!DOCTYPE html>
<html lang="en">
<head>
<meta charset="utf-8">
<title>Heron Design Works – Business Card</title>
<link rel="stylesheet" href="https://fonts.googleapis.com/css2?family=Overlock:wght@400;700&family=Arimo&display=swap">
<style>
  :root {
    --sheet: #ffffff;
    --card-back: #000000;
    --card-front: #8bc541;
    --uv-tone: #84b83f;
    --brand-green: #8bc541;
    --ink: #2f3d12;
    --label: #000000;
  }
  * { margin: 0; padding: 0; box-sizing: border-box; }
  html, body { width: 1200px; height: 1000px; overflow: hidden; background: var(--sheet); }
  .sheet { position: relative; width: 1200px; height: 1000px; }

  .card { position: absolute; width: 720px; height: 460px; }
  .card-back { left: 85px; top: 75px; background: var(--card-back); }
  .card-front { left: 400px; top: 440px; background: var(--card-front); }

  .brand {
    position: absolute; left: 0; right: 0; top: 0; bottom: 0;
    display: flex; align-items: center; justify-content: center; gap: 26px;
  }
  .brand-dot { width: 70px; height: 70px; border-radius: 50%; background: var(--brand-green); }
  .brand-name {
    font-family: "Overlock", sans-serif; font-weight: 400; font-size: 58px;
    color: var(--brand-green); letter-spacing: 1px;
  }

  .uv-spot {
    position: absolute; left: 45px; top: 40px; width: 330px; height: 400px;
    border-radius: 50%; background: var(--uv-tone);
  }
  .holder {
    position: absolute; left: 452px; top: 98px;
    font-family: "Overlock", sans-serif; font-size: 23px; line-height: 33px; color: var(--ink);
  }
  .contact {
    position: absolute; left: 460px; top: 292px;
    font-family: "Overlock", sans-serif; font-size: 19px; line-height: 23px; color: var(--ink);
  }

  .label { position: absolute; font-family: "Arimo", sans-serif; color: var(--label); }
  .label-back { left: 830px; top: 88px; font-size: 30px; }
  .label-front { left: 330px; top: 888px; font-size: 30px; }
  .label-note { left: 757px; top: 926px; font-size: 19px; }
</style>
</head>
<body>
<main class="sheet">
  <section class="card card-back" aria-label="Card back">
    <div class="brand">
      <span class="brand-dot"></span>
      <span class="brand-name">Heron Design Works</span>
    </div>
  </section>
  <span class="label label-back">back</span>

  <section class="card card-front" aria-label="Card front">
    <div class="uv-spot" role="img" aria-label="Spot UV brand decoration"></div>
    <div class="holder">
      <p>Mara Ellison</p>
      <p>Product Designer</p>
    </div>
    <div class="contact">
      <p>M: +112 47120386</p>
      <p>P: 011-36490215</p>
      <p>hello@heronmail.com</p>
      <p>www.herondesign.com</p>
    </div>
  </section>
  <span class="label label-front">front</span>
  <span class="label label-note">here the heron icon will be UV</span>
</main>
</body>
</html>
```